Lumaform website scandinavian interior design

Existing website: http://lumaform-example.no/

Webdesign for interior designer Ragna Tvedtholm. The company name is Lumaform. Scandinavian interiør is known to be simple and elegant. The website will be in Norwegian, we are working on the text. The website needs to have a few more pages than just the front page. Here are the different titles of the pages:

1. Hjem
2. Om Lumaform
3. Tjenester og priser
4.. Kontakt oss

There should be Facebook and Instagram icons somewhere at the bottom of the website.

The logo we want to use is attached (pink with black print, see attachment )

We have attached images for inspiration. We want to use some of these colors. The color in the logo, The style should be elegant, modern and delicate.

It is imprtant that the website is user friendly.

Target Market(s)

People who want to decorate their home
Companies and public sector who need to redecorate

Industry/Entity Type

Interior Designer

Coding

Coded - Design and coding required

Number of Pages Required

5+ page

Font styles to use
Other font styles liked:
• see example in the logo breakdown

Requirements
Must have
• Elegant, modern and delicate design
Images of design, see examples attached
Colors similar to the pictures
Should not have
• Too bright colors
Pictures of people

```html
<!DOCTYPE html>
<html lang="en">
<head>
<meta charset="utf-8">
<title>Lumaform – Scandinavian Interior Design</title>
<link rel="stylesheet" href="https://fonts.googleapis.com/css2?family=Merienda:wght@400;700&family=Tinos:ital,wght@0,400;0,700;1,400;1,700&display=swap">
<style>
:root{
  --blush:#e9c8be;
  --blush-soft:#f3e0da;
  --espresso:#2b1011;
  --espresso-deep:#220b0c;
  --ink:#222;
  --muted:#6d6463;
  --line:#b9a9a6;
  --white:#fff;
}
*{box-sizing:border-box;margin:0;padding:0}
html,body{width:1200px;height:3104px;overflow:hidden}
body{position:relative;background:var(--white);font-family:"Tinos",serif;color:var(--ink)}
.abs{position:absolute}
.heading{font-family:"Merienda",cursive;font-weight:400;color:var(--ink);text-align:center}
.rule{position:absolute;left:560px;width:80px;height:2px;background:var(--ink)}
.btn{position:absolute;background:var(--espresso);color:var(--white);font-family:"Merienda",cursive;font-size:17px;display:flex;align-items:center;justify-content:center;border:2px solid var(--espresso);box-shadow:inset 0 0 0 3px var(--espresso),inset 0 0 0 4px #8a6a6a}
.copy{font-size:15.5px;line-height:1.55;color:var(--muted)}

/* hero */
.hero-band{left:0;top:0;width:1200px;height:380px;background:var(--blush)}
.nav{left:0;top:0;width:1200px;height:56px;font-size:16px}
.nav a{position:absolute;top:22px;color:var(--ink);text-decoration:none;transform:translateX(-50%)}
.nav .active{border-bottom:2px solid var(--ink);padding-bottom:4px}
.nav-logo{position:absolute;left:600px;top:10px;transform:translateX(-50%);font-size:20px;color:var(--espresso);display:flex;align-items:center;gap:6px}
.nav-logo span.mark{width:10px;height:10px;border:1.5px solid var(--espresso);border-radius:50%}
.hero-photo{left:120px;top:128px;width:480px;height:372px;background:linear-gradient(120deg,#2f5a5c 0%,#3b6c6d 45%,#7a8a86 70%,#c9b9a8 100%)}
.hero-title{left:700px;top:152px;width:420px;font-family:"Merienda",cursive;font-weight:700;font-size:34px;line-height:1.2;color:var(--ink)}
.hero-sub{left:700px;top:262px;width:330px;font-size:14px;line-height:1.3;color:var(--muted);text-align:center}

/* about */
.about-text{left:160px;top:684px;width:880px;text-align:center}

/* services */
.card{top:1100px;width:300px;height:390px;background:var(--white);box-shadow:0 2px 8px rgba(0,0,0,.12)}
.card-photo{width:100%;height:192px}
.card h3{font-family:"Tinos",serif;font-style:italic;font-weight:700;font-size:19px;text-align:center;margin:22px 0 14px}
.card p{padding:0 22px}

/* blog */
.blog-band{left:0;top:1568px;width:1200px;height:524px;background:linear-gradient(90deg,#f6e6e1 0%,#eccdc4 100%)}
.blog-photo{left:600px;top:1568px;width:600px;height:524px;background:linear-gradient(180deg,#ecd6cf 0%,#e3c0b6 55%,#c98a87 75%,#b77b78 100%)}
.blog-title{left:128px;top:1728px;font-family:"Merienda",cursive;font-size:32px}
.blog-lead{left:128px;top:1820px;width:420px;font-style:italic;font-weight:700;font-size:17px;line-height:1.25}
.blog-text{left:128px;top:1884px;width:420px}
.blog-arrow{left:172px;top:2012px}

/* contact */
.field{position:absolute;border:1px solid #777;background:var(--white);font-size:12px;padding:6px 8px;color:#444}

/* footer */
.footer{left:0;top:2668px;width:1200px;height:436px;background:var(--espresso-deep);color:var(--white)}
.foot-logo{position:absolute;left:600px;top:56px;transform:translateX(-50%);font-size:46px;display:flex;align-items:center;gap:14px;letter-spacing:1px}
.foot-logo .mark{width:14px;height:14px;border:2px solid var(--white)}
.foot-nav{position:absolute;left:0;top:202px;width:1200px;display:flex;justify-content:center;gap:48px;font-size:17px}
.foot-addr{position:absolute;left:0;top:254px;width:1200px;text-align:center;font-size:16px}
.foot-copy{position:absolute;left:0;top:306px;width:1200px;text-align:center;font-size:13px}
.social{position:absolute;top:354px;width:26px;height:26px;border-radius:50%;border:1.5px solid var(--white)}
</style>
</head>
<body>

<section class="hero">
  <div class="abs hero-band"></div>
  <nav class="abs nav">
    <a class="active" style="left:140px">Home</a>
    <a style="left:320px">About Lumaform</a>
    <a style="left:464px">Services</a>
    <div class="nav-logo"><span class="mark"></span>Lumaform</div>
    <a style="left:772px">prices</a>
    <a style="left:916px">Contact us</a>
    <a style="left:1048px">Eng ▾</a>
  </nav>
  <div class="abs hero-photo" role="img" aria-label="Living room with teal walls, a blue sofa and a framed painting"></div>
  <h1 class="abs hero-title">Need help developing interior environments</h1>
  <p class="abs hero-sub">Company Lumaform AS is working on the development of interior environments for private</p>
  <div class="btn" style="left:788px;top:412px;width:164px;height:60px">Get Started</div>
</section>

<section class="about">
  <h2 class="abs heading" style="left:0;top:584px;width:1200px;font-size:34px">About Lumaform</h2>
  <div class="rule" style="top:648px"></div>
  <p class="abs copy about-text">Lorem ipsum dolor sit amet, consectetur adipiscing elit, sed do eiusmod tempor incididunt ut labore et dolore magna aliqua. Ut enim ad minim veniam, quis nostrud exercitation ullamco laboris nisi ut aliquip ex ea commodo consequat. Duis aute irure dolor in reprehenderit in voluptate velit esse cillum dolore eu fugiat nulla pariatur. Excepteur sint occaecat cupidatat non proident, sunt in culpa qui officia deserunt mollit anim id est laborum.</p>
  <div class="btn" style="left:512px;top:820px;width:176px;height:60px">Learn More</div>
</section>

<section class="services">
  <h2 class="abs heading" style="left:0;top:974px;width:1200px;font-size:34px">Our Services</h2>
  <div class="rule" style="top:1036px"></div>
  <article class="abs card" style="left:112px">
    <div class="card-photo" role="img" aria-label="Public washroom with purple walls and white basins" style="background:linear-gradient(160deg,#5a4a7a,#8a7fa0 60%,#d8d4d8)"></div>
    <h3>public</h3>
    <p class="copy">Lorem ipsum dolor sit amet, conse ctetur adipiscing elit, sed do eiusmod tempor incididunt ut labore et dolore magna aliqua. Ut eni.</p>
  </article>
  <article class="abs card" style="left:440px">
    <div class="card-photo" role="img" aria-label="Private bathroom with dark wood cabinets and warm lighting" style="background:linear-gradient(160deg,#3a1d14,#7a3a22 55%,#c08a5e)"></div>
    <h3>Private</h3>
    <p class="copy">Lorem ipsum dolor sit amet, conse ctetur adipiscing elit, sed do eiusmod tempor incididunt ut labore et dolore magna aliqua. Ut eni.</p>
  </article>
  <article class="abs card" style="left:764px">
    <div class="card-photo" role="img" aria-label="Bright corporate lounge with patterned wall and plants" style="background:linear-gradient(160deg,#d9d3c6,#b8b2a4 55%,#5d6a55)"></div>
    <h3>Corporate</h3>
    <p class="copy">Lorem ipsum dolor sit amet, conse ctetur adipiscing elit, sed do eiusmod tempor incididunt ut labore et dolore magna aliqua. Ut eni.</p>
  </article>
</section>

<section class="blog">
  <div class="abs blog-band"></div>
  <div class="abs blog-photo" role="img" aria-label="Pink velvet sofa with brass coffee table and pendant lamps"></div>
  <h2 class="abs blog-title">Our Latest Blog</h2>
  <p class="abs blog-lead">Lorem ipsum dolor sit amet, consectetur adip elit, sed do eiusmod tempor</p>
  <p class="abs copy blog-text">Lorem ipsum dolor sit amet, consectetur adipiscing elit, sed do eiusmod tempor incididunt ut labore et dolore magna aliqua. Ut enim ad minim veniam, quis nostrud exercitation ullamco.</p>
  <svg class="abs blog-arrow" width="30" height="12" viewBox="0 0 30 12" aria-label="Read more"><path d="M0 6h27M22 1l6 5-6 5" fill="none" stroke="#222" stroke-width="2"/></svg>
</section>

<section class="contact">
  <h2 class="abs heading" style="left:0;top:2176px;width:1200px;font-size:34px">Get In Touch</h2>
  <div class="rule" style="top:2240px"></div>
  <div class="field" style="left:384px;top:2288px;width:208px;height:40px">First Name</div>
  <div class="field" style="left:612px;top:2288px;width:208px;height:40px">Last Name</div>
  <div class="field" style="left:384px;top:2344px;width:208px;height:40px">Email</div>
  <div class="field" style="left:612px;top:2344px;width:208px;height:40px">Phone</div>
  <div class="field" style="left:384px;top:2392px;width:436px;height:90px">Message</div>
  <div class="btn" style="left:516px;top:2512px;width:168px;height:56px">Submit&nbsp;<svg width="14" height="12" viewBox="0 0 14 12"><path d="M1 1l12 5-12 5 2-5z" fill="#fff"/></svg></div>
</section>

<footer class="abs footer">
  <div class="foot-logo"><span class="mark"></span>Lumaform</div>
  <div class="foot-nav"><span>Home</span><span>About Us</span><span>Services</span><span>Price</span><span>Contact Us</span></div>
  <div class="foot-addr">
    <svg width="14" height="18" viewBox="0 0 14 18" style="vertical-align:-3px;margin-right:10px"><path d="M7 0C3 0 0 3 0 7c0 5 7 11 7 11s7-6 7-11c0-4-3-7-7-7z" fill="#fff"/><circle cx="7" cy="7" r="2.5" fill="#220b0c"/></svg>lumaform-example.no v / Ragna Tvedtholm Lyngveien 14 2381 Solberg
  </div>
  <div class="foot-copy">© Copyright 2022 Lumaform &nbsp;|&nbsp; All Rights Reserved</div>
  <span class="social" style="left:544px" aria-label="Social profile link"></span>
  <span class="social" style="left:587px" aria-label="Social profile link"></span>
  <span class="social" style="left:630px" aria-label="Social profile link"></span>
</footer>

</body>
</html>
```